Faith Based Film Production Ecommerce Site Needed

We are a faith based film production company that offers coaching services as well as physical and digital products.

We have a Wordpress site on Hostwren. It currently, features a landing page (https://brightlampstudio.net/), however we now need a fully fleshed out interactive website that will feature short videos/trailers as well the ability for customers to make online purchases.

The updated site will feature 5 tabs - Take 1, Take 2, Take 3, BTS and Contact. This toolbar/menu should remain fixed/stable while visitors navigate the different tabs/pages, as shown here - https://pelmarokane.com/ (note this site is JUST a reference for its unmoving menu/toolbar in the top right corner of the page).

The text for each tab and actual video content will be provided for potential candidates. Until then, please improvise.

There will be 5 short trailers/reels featured under the "Take 2" tab, that will be shown as thumbnails the same size found here - https://pelmarokane.com/see-pel-at-work/ (reference for thumbnail size only). The names of these trailers will be called, Lamp Summons, Lamp Flourish, Lamp Dawn, Lamp Hearth, and Lamp Courtship.

Lastly, when arriving onto the page, visitors will be greeted with a inaudible video loop, similar to the one found here - https://www.tq-moviehouse.com/ (Note - this is a reference simply to show inaudible video looping). The ACTUAL video to be used however can be found here - https://clipvaultr.net/manage/videos/473918265, beginning at the 15 second mark when the 3 people are entering the cinema and ending at the 28 second mark where the screen gradually fades to black. The video will then consistently re-loop.

Once again, more detail will be provided for the most interesting submissions and of course, official winner.

Should you have any questions until then, please do not hesitate to reach out.

```html
<!DOCTYPE html>
<html lang="en">
<head>
<meta charset="utf-8">
<title>Bright Lamp — Video Production</title>
<link rel="stylesheet" href="https://fonts.googleapis.com/css2?family=League+Spartan:wght@400;600;700&family=Poppins:wght@300;400;500;600&display=swap">
<style>
:root{
  --ink:#111;
  --white:#fff;
  --forest:#1d3330;
  --grey-band:#cfcfcf;
  --light:#f3f3f3;
  --line:#9a9a9a;
  --star:#f5b400;
  --night:#1a2233;
  --head:"League Spartan",sans-serif;
  --body:"Poppins",sans-serif;
}
*{margin:0;padding:0;box-sizing:border-box}
html,body{width:1200px;height:4608px;overflow:hidden;background:var(--white);font-family:var(--body);color:var(--ink)}
.page{position:relative;width:1200px;height:4608px}
.abs{position:absolute}
.ph{position:absolute}
.btn{position:absolute;border:2px solid var(--ink);font-size:12px;display:flex;align-items:center;justify-content:center;background:transparent}

/* hero */
.hero{position:absolute;left:0;top:0;width:1200px;height:623px}
.hero-media{position:absolute;inset:0;background:linear-gradient(135deg,#0f1a3a 0%,#203a6e 45%,#0b1122 100%);clip-path:polygon(451px 0,1200px 0,1200px 623px,630px 623px)}
.brand{position:absolute;left:116px;top:8px;width:116px;text-align:center;font-family:var(--head);font-weight:700;font-size:13px;letter-spacing:.5px}
.brand .mark{display:block;width:28px;height:28px;margin:0 auto 6px;background:var(--ink)}
.nav{position:absolute;top:30px;left:537px;font-size:12px;color:var(--white)}
.nav span{position:absolute;white-space:nowrap}
.nav .active{border-bottom:2px solid var(--white);padding-bottom:4px}
.nav-cta{position:absolute;left:954px;top:14px;width:132px;height:45px;border:2px solid var(--white);color:var(--white);font-size:12px;display:flex;align-items:center;justify-content:center}
.play-big{position:absolute;left:836px;top:260px}
.hero h1{position:absolute;left:114px;top:205px;font-family:var(--head);font-weight:700;font-size:60px;line-height:68px}
.hero h1 .hollow{color:transparent;-webkit-text-stroke:2px var(--ink);font-weight:600}
.hero p{position:absolute;left:114px;top:354px;width:420px;font-size:14px;line-height:21px}

/* partners */
.partners{position:absolute;left:0;top:623px;width:1200px;height:125px}
.rating{position:absolute;left:0;top:0;width:315px;height:125px;background:var(--forest);color:var(--white)}
.rating .badge{position:absolute;left:112px;top:26px;width:38px;height:38px;border-radius:50%;background:#e6e6e6}
.rating .stars{position:absolute;left:168px;top:26px;font-size:26px;color:var(--star);letter-spacing:2px}
.rating .cap{position:absolute;left:112px;top:72px;font-size:10px;line-height:15px}
.client{position:absolute;top:45px;font-family:var(--body);font-size:26px;color:#9b9b9b;font-weight:500;letter-spacing:1px}

/* expertise */
.kicker{position:absolute;font-size:16px;font-weight:500}
.h2{position:absolute;font-family:var(--head);font-weight:600;font-size:36px;line-height:40px}
.copy{position:absolute;font-size:11.5px;line-height:20.5px}
.stat{position:absolute;top:1114px}
.stat b{display:block;font-family:var(--head);font-size:30px;font-weight:600}
.stat small{display:block;font-size:11px;line-height:14px;margin-top:4px}

/* team */
.team{position:absolute;left:0;top:1351px;width:1200px;height:662px;background:var(--grey-band)}
.giant{position:absolute;width:1200px;text-align:center;font-family:var(--head);font-weight:700;font-size:112px;color:var(--white);letter-spacing:1px}

/* process */
.lead{position:absolute;font-size:21px;line-height:32px}
.check{position:absolute;left:120px;font-size:14px;font-weight:500;padding-left:30px;line-height:21px}
.check svg{position:absolute;left:0;top:3px}
.step{position:absolute;left:637px;width:451px;height:56px;border-bottom:2px solid var(--line)}
.step span{position:absolute;left:0;top:18px;font-size:20px;font-weight:500}
.step b{position:absolute;right:0;top:6px;font-family:var(--head);font-size:42px;font-weight:600}

/* reels */
.thumb{position:absolute;top:2628px;width:188px;height:186px}
.thumb svg{position:absolute;left:70px;top:68px}
.reel-name{position:absolute;top:2832px;font-size:14px;font-weight:500}

/* projects */
.projects{position:absolute;left:0;top:2907px;width:1200px;height:367px;background:var(--light)}

/* testimonial */
.quote{position:absolute;left:0;top:3274px;width:1200px;height:471px;background:radial-gradient(ellipse at 70% 40%,#3a4a5e 0%,var(--night) 55%,#080b12 100%);color:var(--white);text-align:center}

/* contact */
.field{position:absolute;border:1.5px solid #999;font-size:11px;color:#888;padding:14px 16px}
.send{position:absolute;left:483px;top:4120px;width:172px;height:50px;background:var(--ink);color:var(--white);font-size:12px;display:flex;align-items:center;justify-content:center}

/* footer */
.footer{position:absolute;left:0;top:4222px;width:1200px;height:386px;background:var(--forest);color:var(--white)}
.addr{position:absolute;font-size:12px;line-height:20px}
.award{position:absolute;left:896px;width:190px;background:#e9e9e9}
.social{position:absolute;left:118px;top:300px;font-size:13px;font-weight:600;display:flex;gap:18px;align-items:center}
</style>
</head>
<body>
<div class="page">

<header class="hero">
  <div class="hero-media" role="img" aria-label="Dim cinema corridor with people walking in, video loop"></div>
  <div class="brand"><span class="mark"></span>BRIGHT LAMP</div>
  <nav class="nav">
    <span class="active" style="left:0">Home</span>
    <span style="left:68px">Take 1</span>
    <span style="left:139px">Take 2</span>
    <span style="left:211px">Take 3</span>
    <span style="left:281px">BTS</span>
    <span style="left:338px">Contact</span>
  </nav>
  <div class="nav-cta">Start a Project</div>
  <svg class="play-big" width="94" height="94" viewBox="0 0 94 94"><circle cx="47" cy="47" r="44" fill="none" stroke="#fff" stroke-width="4"/><path d="M37 28 L67 47 L37 66Z" fill="#fff"/></svg>
  <h1>We Bring Your<br><span class="hollow">Brand to Life</span></h1>
  <p>Custom video content to capture the attention of your audience like no other content can.</p>
  <div class="btn" style="left:114px;top:422px;width:126px;height:40px">Start a Project</div>
  <div class="btn" style="left:256px;top:422px;width:132px;height:40px">Recent Work</div>
</header>

<section class="partners">
  <div class="rating">
    <span class="badge"></span>
    <span class="stars">★★★★★</span>
    <div class="cap">Premier Searchly Partner<br>5/5 Reviews Rating</div>
  </div>
  <span class="client" style="left:375px">Norvex</span>
  <span class="client" style="left:530px">Kalten</span>
  <span class="client" style="left:630px">PAGEWELL</span>
  <span class="client" style="left:843px">orvista</span>
  <span class="client" style="left:1050px;font-size:22px">HALBROOK</span>
</section>

<section class="expertise">
  <div class="kicker" style="left:120px;top:872px">Proven Results</div>
  <h2 class="h2" style="left:120px;top:900px;width:400px">Our expertise where you need it most</h2>
  <p class="copy" style="left:120px;top:986px;width:380px">Do you know what you want your brand to say, but just not sure how to say it? Or maybe you know you need a more interactive marketing strategy, but not sure where to start? Our video content shows buyers exactly what your brand is, does and offers the world. Our videos move your marketing forward.</p>
  <div class="stat" style="left:120px"><b>180+</b><small>5 Star<br>Reviews</small></div>
  <div class="stat" style="left:238px"><b>50K</b><small>Videos<br>Produced</small></div>
  <div class="stat" style="left:355px"><b>35+</b><small>Years of<br>Experience</small></div>
  <div class="btn" style="left:114px;top:1222px;width:131px;height:40px">Work with Us</div>
  <div class="ph" style="left:608px;top:787px;width:592px;height:512px;background:linear-gradient(160deg,#d9d4cc 0%,#8f8a86 50%,#3b3f44 100%)" role="img" aria-label="Video editor working at a desk with a monitor showing an editing timeline"></div>
</section>

<section class="team">
  <div class="giant" style="top:45px">We're Here To</div>
  <div class="ph" style="left:313px;top:89px;width:134px;height:447px;background:linear-gradient(#8b2b2b,#3f5a7a 60%,#9a6a2e)" role="img" aria-label="Camera operator holding a camera"></div>
  <div class="ph" style="left:537px;top:89px;width:143px;height:447px;background:linear-gradient(#2a2a2a,#111)" role="img" aria-label="Presenter in a dark suit"></div>
  <div class="ph" style="left:778px;top:89px;width:143px;height:447px;background:linear-gradient(#333,#161616)" role="img" aria-label="Crew member holding a clapperboard"></div>
  <div class="giant" style="top:365px">Help You</div>
  <div class="btn" style="left:533px;top:563px;width:134px;height:42px;font-size:12px">Meet The Team</div>
</section>

<section class="process">
  <h2 class="h2" style="left:120px;top:2068px;width:440px;line-height:50px">Straightforward 5 step easy process</h2>
  <p class="lead" style="left:120px;top:2178px;width:420px">Take your video marketing strategy from 0 to 120 miles per hour.</p>
  <p class="copy" style="left:120px;top:2262px;width:410px;font-size:11px">Our team of video production experts walk you through every aspect of the video design and development process. Once your content is captured, we customize your video by incorporating imagery, music, locations and an overall feel consistent with your brand – so that every aspect of your video reflects its personality, unique attributes and defining services and products.</p>
  <div class="check" style="top:2405px"><svg width="14" height="12" viewBox="0 0 14 12"><path d="M1 6 L5 10 L13 1" fill="none" stroke="#111" stroke-width="2.5"/></svg>7-10 day turnaround</div>
  <div class="check" style="top:2440px"><svg width="14" height="12" viewBox="0 0 14 12"><path d="M1 6 L5 10 L13 1" fill="none" stroke="#111" stroke-width="2.5"/></svg>1000+ satisfied clients</div>
  <div class="check" style="top:2475px"><svg width="14" height="12" viewBox="0 0 14 12"><path d="M1 6 L5 10 L13 1" fill="none" stroke="#111" stroke-width="2.5"/></svg>Highest rated video production<br>agency in the midwest</div>

  <div class="step" style="top:2091px"><span>Discovery Call</span><b>01</b></div>
  <div class="step" style="top:2182px"><span>Pre-Production</span><b>02</b></div>
  <div class="step" style="top:2273px"><span>On-Site Production/Editing</span><b>03</b></div>
  <div class="step" style="top:2364px"><span>Final Delivery</span><b>04</b></div>
  <div class="step" style="top:2454px"><span>Client Satisfaction</span><b>05</b></div>
</section>

<section class="reels">
  <h2 class="h2" style="left:120px;top:2565px">Take 2</h2>
  <div class="thumb" style="left:120px;background:linear-gradient(#d8c3b0,#8a6a55)" role="img" aria-label="Lamp Summons reel thumbnail"><svg width="48" height="48" viewBox="0 0 48 48"><circle cx="24" cy="24" r="21" fill="rgba(255,255,255,.35)" stroke="#fff" stroke-width="2.5"/><path d="M19 14 L34 24 L19 34Z" fill="#fff"/></svg></div>
  <div class="thumb" style="left:315px;background:linear-gradient(#b9a98c,#4f5c5a)" role="img" aria-label="Lamp Flourish reel thumbnail"><svg width="48" height="48" viewBox="0 0 48 48"><circle cx="24" cy="24" r="21" fill="rgba(255,255,255,.35)" stroke="#fff" stroke-width="2.5"/><path d="M19 14 L34 24 L19 34Z" fill="#fff"/></svg></div>
  <div class="thumb" style="left:509px;background:linear-gradient(#8a6a4a,#d9c5ae)" role="img" aria-label="Lamp Dawn reel thumbnail"><svg width="48" height="48" viewBox="0 0 48 48"><circle cx="24" cy="24" r="21" fill="rgba(255,255,255,.35)" stroke="#fff" stroke-width="2.5"/><path d="M19 14 L34 24 L19 34Z" fill="#fff"/></svg></div>
  <div class="thumb" style="left:703px;background:linear-gradient(#b8c9d8,#7a6a4e 55%,#5f8a3a)" role="img" aria-label="Lamp Hearth reel thumbnail"><svg width="48" height="48" viewBox="0 0 48 48"><circle cx="24" cy="24" r="21" fill="rgba(255,255,255,.35)" stroke="#fff" stroke-width="2.5"/><path d="M19 14 L34 24 L19 34Z" fill="#fff"/></svg></div>
  <div class="thumb" style="left:898px;background:linear-gradient(#c9c3bd,#3a2e2a 60%,#b06a2c)" role="img" aria-label="Lamp Courtship reel thumbnail"><svg width="48" height="48" viewBox="0 0 48 48"><circle cx="24" cy="24" r="21" fill="rgba(255,255,255,.35)" stroke="#fff" stroke-width="2.5"/><path d="M19 14 L34 24 L19 34Z" fill="#fff"/></svg></div>
  <div class="reel-name" style="left:118px">Lamp Summons</div>
  <div class="reel-name" style="left:313px">Lamp Flourish</div>
  <div class="reel-name" style="left:508px">Lamp Dawn</div>
  <div class="reel-name" style="left:702px">Lamp Hearth</div>
  <div class="reel-name" style="left:897px">Lamp Courtship</div>
</section>

<section class="projects">
  <h2 class="h2" style="left:120px;top:116px">Recent Projects</h2>
  <p class="copy" style="left:122px;top:170px;width:280px;font-size:10.5px;line-height:20px">We offer an all-hands-on-deck agency, offering a fun, simple and quick process from start to finish that result in more leads, more sales, and more business.</p>
  <div class="ph" style="left:428px;top:54px;width:230px;height:259px;background:linear-gradient(#e4ddd6,#8e8781)" role="img" aria-label="Phone on a tripod filming a creator"></div>
  <div class="ph" style="left:673px;top:54px;width:230px;height:259px;background:radial-gradient(circle at 50% 45%,#f1e6da 0,#2b2b2b 45%,#b36a34 75%)" role="img" aria-label="Ring light with a phone mounted in the centre"></div>
  <div class="ph" style="left:916px;top:54px;width:231px;height:259px;background:linear-gradient(#e8e8e8,#d7b63a 60%,#3d5f8a)" role="img" aria-label="Two creators filming in a bright kitchen"></div>
  <div class="ph" style="left:1159px;top:54px;width:41px;height:259px;background:linear-gradient(#d9d0c6,#8a4a3a)" role="img" aria-label="Further project preview"></div>
  <svg class="abs" style="left:522px;top:163px" width="40" height="40" viewBox="0 0 40 40"><circle cx="20" cy="20" r="18" fill="#fff"/><path d="M16 12 L28 20 L16 28Z" fill="#111"/></svg>
  <svg class="abs" style="left:768px;top:163px" width="40" height="40" viewBox="0 0 40 40"><circle cx="20" cy="20" r="18" fill="#fff"/><path d="M16 12 L28 20 L16 28Z" fill="#111"/></svg>
  <svg class="abs" style="left:1011px;top:163px" width="40" height="40" viewBox="0 0 40 40"><circle cx="20" cy="20" r="18" fill="#fff"/><path d="M16 12 L28 20 L16 28Z" fill="#111"/></svg>
</section>

<section class="quote" role="img" aria-label="Athlete training in a dark gym with stage lights">
  <svg class="abs" style="left:572px;top:101px" width="58" height="58" viewBox="0 0 58 58"><circle cx="29" cy="29" r="26" fill="none" stroke="#fff" stroke-width="3"/><text x="29" y="43" text-anchor="middle" font-family="League Spartan,sans-serif" font-weight="700" font-size="34" fill="#fff">“</text></svg>
  <p class="abs" style="left:290px;top:198px;width:620px;font-size:11.5px;line-height:20px">Lorem ipsum dolor sit amet, consectetur adipiscing elit. Suspendisse vitae mi ut dolor tincidunt rhoncus malesuada sit amet quam. Vivamus eget lacinia neque. Etiam et semper mi, in finibus justo. Donec placerat mauris sit amet interdum varius. Quisque commodo felis eu ex congue, ut tristique lacus egestas.</p>
  <div class="abs" style="left:0;width:1200px;top:278px;font-size:24px;color:var(--star);letter-spacing:2px">★★★★★</div>
  <div class="abs" style="left:0;width:1200px;top:330px;font-size:15px;font-weight:500">Marisol Venn</div>
</section>

<section class="contact">
  <h2 class="h2" style="left:120px;top:3839px;font-size:34px">Let's Work <span style="font-weight:400">Together</span></h2>
  <p class="copy" style="left:122px;top:3902px;width:330px;font-size:11px">Lorem ipsum dolor sit amet, consectetur adipiscing elit, sed do eiusmod tempor incididunt ut labore et dolore magna aliqua. Quis ipsum suspendisse ultrices gravida. Risus commodo viverra maecenas accumsan lacus vel facilisis.</p>
  <div class="field" style="left:483px;top:3809px;width:292px;height:46px">First Name</div>
  <div class="field" style="left:789px;top:3809px;width:299px;height:46px">Last Name</div>
  <div class="field" style="left:483px;top:3871px;width:292px;height:47px">Email</div>
  <div class="field" style="left:789px;top:3871px;width:299px;height:47px">Phone</div>
  <div class="field" style="left:483px;top:3934px;width:605px;height:166px">Your Message</div>
  <div class="send">Send Message</div>
</section>

<footer class="footer">
  <div class="abs" style="left:118px;top:62px;width:100px;text-align:center;font-family:var(--head);font-weight:700;font-size:15px"><span style="display:block;width:34px;height:34px;margin:0 auto 10px;background:var(--white)"></span>BRIGHT LAMP</div>
  <p class="abs" style="left:118px;top:162px;width:350px;font-size:11px;line-height:20px">Lorem ipsum dolor sit amet, consectetur adipiscing elit. Suspendisse vitae mi ut dolor tincidunt rhoncus malesuada sit amet quam. Vivamus eget lacinia neque. Etiam et semper mi, in finibus justo. Donec placerat mauris sit amet interdum varius. Quisque com.</p>
  <div class="addr" style="left:531px;top:124px">Lorem ipsum dolor<br>Brookmere, IL 60412<br>555-010-2846</div>
  <div class="addr" style="left:719px;top:124px">Lorem ipsum dolor<br>Brookmere, IL 60412<br>555-010-2846</div>
  <div class="addr" style="left:531px;top:217px">Lorem ipsum dolor<br>Brookmere, IL 60412<br>555-010-2846</div>
  <div class="addr" style="left:719px;top:217px">Lorem ipsum dolor<br>Brookmere, IL 60412<br>555-010-2846</div>
  <div class="award" style="top:129px;height:68px"></div>
  <div class="award" style="top:217px;height:87px;background:#3c4a66"></div>
  <div class="social">
    <span>Pagewell</span><span>Chirper</span><span>Snapgrid</span><span>Vidstream</span><span>Linkwork</span><span>Reelbox</span>
    <svg width="30" height="22" viewBox="0 0 30 22"><rect x="1" y="1" width="28" height="20" fill="#fff"/><path d="M2 2 L15 12 L28 2" fill="none" stroke="#1d3330" stroke-width="2.5"/></svg>
  </div>
  <div class="abs" style="left:118px;top:352px;font-size:10px">Copyright 2023 Bright Lamp | All Rights Reserved</div>
</footer>

</div>
</body>
</html>
```